Flyer design needed for services offered and to show reviews from previous customers

I would like a Flyer designed showing some of the services i offer:
-LED lighting upgrades (pot lights, accent & commercial)
-Electrical repairs & Service work
- Fayglowen lighting
- TV wall mounts
My website is Voltarisa.ca if you need any photos from there in higher quality please let me know and i can provide them.

I want it to have a couple reviews from previous customers (attached links to facebook and google page)
Google:
https://revpage.example/r/QZ8kd4mtpWhaJXo/review
Facebook:
https://www.socialbook.example/Voltarisa-Contracting-Ltd-552918730461283

```html
<!DOCTYPE html>
<html lang="en">
<head>
<meta charset="utf-8">
<title>Voltarisa Contracting Ltd – Services Flyer</title>
<link href="https://fonts.googleapis.com/css2?family=Teko:wght@400;500;600&family=Source+Sans+3:wght@400;600&display=swap" rel="stylesheet">
<style>
  :root {
    --orange: #f07a0c;
    --orange-deep: #e06a05;
    --black: #0d0d0d;
    --white: #ffffff;
    --paper: #fbfbfb;
    --footer-grey: #e9e9e9;
    --backdrop: #dfe3e8;
    --ink: #1a1a1a;
  }
  * { box-sizing: border-box; margin: 0; padding: 0; }
  html, body { width: 1200px; height: 900px; overflow: hidden; }
  body { background: var(--backdrop); position: relative; font-family: "Source Sans 3", Arial, sans-serif; }

  .flyer {
    position: absolute; left: 320px; top: 55px; width: 560px; height: 790px;
    background: linear-gradient(180deg, var(--white) 0%, var(--paper) 60%, #f1f1f1 100%);
    box-shadow: 0 6px 18px rgba(0,0,0,.18); overflow: hidden;
  }
  .headline { position: absolute; left: 0; right: 0; top: 32px; text-align: center; white-space: nowrap;
    font-family: "Teko", "Arial Narrow", sans-serif; font-weight: 500; line-height: 1; text-transform: uppercase; }
  .headline .line-accent { display: block; color: var(--orange); font-size: 33px; }
  .headline .line-main { display: block; color: var(--black); font-size: 33px; margin-top: 12px; }

  .photo-band { position: absolute; left: 0; right: 0; top: 176px; height: 22px; background: var(--black); }
  .tile { position: absolute; top: 128px; width: 152px; height: 159px; }
  .tile--left { left: 43px; background: linear-gradient(180deg, #3e5a6c 0%, #c9c2b5 38%, #e8e3da 70%, #b9a88f 100%); }
  .tile--right { left: 361px; background: linear-gradient(180deg, #d9dde0 0%, #8d9498 45%, #55595b 75%, #8a6a48 100%); }
  .tile--brand { left: 202px; background: var(--orange); display: flex; flex-direction: column;
    align-items: center; justify-content: center; gap: 8px; }
  .brand-dot { width: 44px; height: 44px; border-radius: 50%; background: var(--white); }
  .brand-name { font-family: "Teko", "Arial Narrow", sans-serif; font-weight: 500; color: var(--white);
    font-size: 22px; line-height: .95; text-align: center; text-transform: uppercase; letter-spacing: 1px; }

  .services-bg { position: absolute; left: 0; right: 0; top: 400px; height: 210px;
    background: linear-gradient(180deg, #f4f4f4 0%, #dcdcdc 55%, #c9c9c9 100%); opacity: .75; }
  .services-frame { position: absolute; left: 10px; top: 327px; width: 540px; height: 248px;
    border: 1.5px solid var(--orange); }
  .services-title { position: absolute; left: 0; right: 0; top: 306px; text-align: center;
    font-family: "Teko", "Arial Narrow", sans-serif; font-weight: 500; font-size: 36px; line-height: 1; text-transform: uppercase; }
  .services-title span { background: var(--white); padding: 0 10px; color: var(--black); }
  .services-title em { font-style: normal; color: var(--orange); }
  .services-intro { position: absolute; left: 18px; top: 353px; width: 524px; height: 57px; background: var(--black);
    color: var(--white); font-size: 11.5px; line-height: 15px; text-align: center; padding: 4px 10px; }

  .service { position: absolute; display: flex; align-items: center; }
  .service-icon { width: 55px; height: 58px; background: var(--orange); flex: none;
    display: flex; align-items: center; justify-content: center; }
  .service-label { font-size: 12.5px; line-height: 16px; color: var(--ink); text-align: center; font-weight: 600; }
  .service--led { left: 58px; top: 425px; } .service--led .service-label { width: 170px; margin-left: 14px; }
  .service--repair { left: 58px; top: 508px; } .service--repair .service-label { width: 160px; margin-left: 18px; }
  .service--fay { left: 336px; top: 424px; } .service--fay .service-label { margin-left: 13px; }
  .service--tv { left: 336px; top: 504px; } .service--tv .service-label { margin-left: 13px; }

  .review-rule { position: absolute; left: 0; right: 0; top: 607px; height: 5px; background: var(--black); }
  .review-band { position: absolute; left: 0; right: 0; top: 612px; height: 133px;
    background: linear-gradient(90deg, var(--orange) 0%, var(--orange) 50%, var(--orange-deep) 50%, #cc5f07 100%); }
  .review-title { position: absolute; left: 170px; top: 593px; width: 205px; height: 40px; background: var(--black);
    color: var(--white); font-family: "Teko", "Arial Narrow", sans-serif; font-weight: 500; font-size: 27px;
    display: flex; align-items: center; justify-content: center; text-transform: uppercase; padding-top: 4px; }
  .review { position: absolute; top: 650px; height: 80px; color: var(--white); }
  .review p { font-size: 8.6px; line-height: 10.5px; opacity: .92; }
  .review cite { position: absolute; left: 0; top: 62px; display: block; white-space: nowrap; font-style: normal; font-size: 13px; }
  .review cite .stars { letter-spacing: 1px; margin-left: 10px; }
  .review--one { left: 53px; width: 212px; }
  .review--two { left: 284px; width: 260px; }

  .footer { position: absolute; left: 0; right: 0; top: 745px; height: 45px; background: var(--footer-grey);
    font-family: "Teko", "Arial Narrow", sans-serif; font-weight: 500; font-size: 19px; color: var(--black);
    display: flex; justify-content: center; align-items: center; gap: 16px; padding-top: 6px; text-transform: uppercase; }
</style>
</head>
<body>
<main class="flyer">
  <h1 class="headline">
    <span class="line-accent">Our promise is to deliver the best possible</span>
    <span class="line-main">service at fair prices!</span>
  </h1>

  <div class="photo-band"></div>
  <div class="tile tile--left" role="img" aria-label="Photo of a wall-mounted TV above a modern linear fireplace"></div>
  <div class="tile tile--brand">
    <span class="brand-dot"></span>
    <span class="brand-name">Voltarisa<br>Contracting Ltd</span>
  </div>
  <div class="tile tile--right" role="img" aria-label="Photo of a bright living room with pot lights and a corner fireplace"></div>

  <div class="services-bg" role="img" aria-label="Faint background photo of an industrial electrical installation"></div>
  <div class="services-frame"></div>
  <h2 class="services-title"><span>Our <em>Service</em></span></h2>
  <p class="services-intro">Below are some of the Services we provide. If you have a question about something that is not listed below, please don't hesitate to contact us. We are a fully Licensed &amp; Insured Electrical Contractor and we would love the opportunity to help you with your needs.</p>

  <div class="service service--led">
    <div class="service-icon">
      <svg width="38" height="42" viewBox="0 0 38 42" fill="none" stroke="#fff" stroke-width="2" stroke-linecap="round">
        <path d="M12 26V14a7 7 0 0 1 14 0v12"/><path d="M9 26h20"/><path d="M15 26v12M23 26v8"/>
        <path d="M19 2v3M6 8l3 2M32 8l-3 2M3 17h4M31 17h4"/>
      </svg>
    </div>
    <span class="service-label">LED lighting upgrades (pot lights, accent &amp; commercial)</span>
  </div>

  <div class="service service--repair">
    <div class="service-icon">
      <svg width="38" height="44" viewBox="0 0 38 44" fill="none" stroke="#fff" stroke-width="2" stroke-linecap="round">
        <rect x="5" y="4" width="20" height="36" rx="3"/><rect x="9" y="8" width="12" height="7"/>
        <circle cx="15" cy="26" r="5"/><path d="M13 28l4-4"/><path d="M29 10v20M34 10v16"/><path d="M25 36c4 0 4-6 4-6"/>
      </svg>
    </div>
    <span class="service-label">Electrical repairs &amp; Service work</span>
  </div>

  <div class="service service--fay">
    <div class="service-icon">
      <svg width="38" height="44" viewBox="0 0 38 44" fill="none" stroke="#fff" stroke-width="2" stroke-linecap="round">
        <path d="M13 30c0-5-5-7-5-14a11 11 0 0 1 22 0c0 7-5 9-5 14z"/><path d="M14 34h10M15 38h8"/>
        <path d="M16 20l3-5 2 4 2-3"/><path d="M19 1v2M4 8l2 1M34 8l-2 1M1 18h3M34 18h3"/>
      </svg>
    </div>
    <span class="service-label">Fayglowen lighting</span>
  </div>

  <div class="service service--tv">
    <div class="service-icon">
      <svg width="44" height="34" viewBox="0 0 44 34" fill="none" stroke="#fff" stroke-width="2" stroke-linecap="round">
        <rect x="3" y="8" width="38" height="18" rx="2"/><path d="M10 4v26M34 4v26"/><path d="M10 17h24"/>
        <circle cx="17" cy="17" r="2"/><circle cx="27" cy="17" r="2"/>
      </svg>
    </div>
    <span class="service-label">TV wall mounts</span>
  </div>

  <div class="review-band"></div>
  <div class="review-rule"></div>
  <h2 class="review-title">Customer Review</h2>

  <blockquote class="review review--one">
    <p>Rhys did some shop work for me and did a great job. Hooked up a couple of hoists and compressor in an old shop that had several renovations. He figured it out. Was very professional, punctual and fair. I would recommend him and will use him again.</p>
    <cite>-Owen Brackley <span class="stars">★★★★★</span></cite>
  </blockquote>

  <blockquote class="review review--two">
    <p>Hired Rhys to do some electrical in our home. Had two other electricians come in before him and neither could figure out how to do the job. Rhys scoped it out very well and managed to get it all done with no issues. He was on time, kept a very clean work area, was quick, and very pleasant all around. Will be going to him for all our future electrical needs.</p>
    <cite>-Lisette Harlow <span class="stars">★★★★★</span></cite>
  </blockquote>

  <footer class="footer">
    <span>Call us-(555) 014-2286</span>
    <span>Visit us- www.voltarisa.ca</span>
  </footer>
</main>
</body>
</html>
```